Moonquill: Smart Quotes for Wine Lovers

Hello. I am completing book of quotes for wine lovers. Need the text formatted so that it is easy to read and aesthetically pleasing...modern, clean, smart. Number the pages. The cover is complete. Book is small square. 7.5 by 7.5 inches. If you want to show me first few pages that would be awesome. Thank you!
Updates

I edited the quotes so if you downloaded first ones, please grab these ones instead, thank you! 

Target Market(s)

wine lovers. Urban. Modern.

Industry/Entity Type

Quotes

Requirements
Should not have
• No color. black and white only.

```html
<!DOCTYPE html>
<html lang="en">
<head>
<meta charset="utf-8">
<title>Moonquill: Smart Quotes for Wine Lovers</title>
<link rel="stylesheet" href="https://fonts.googleapis.com/css2?family=Cormorant+Infant:ital,wght@1,500&family=Questrial&display=swap">
<style>
  :root {
    --backdrop: #e2e2e2;
    --paper: #ffffff;
    --ink: #111111;
    --edge: #2a2a2a;
    --glass-dark: #9a9a9a;
    --glass-light: #dcdcdc;
    --stem: #b5b5b5;
  }
  * { margin: 0; padding: 0; box-sizing: border-box; }
  html, body {
    width: 1200px; height: 900px; overflow: hidden;
    background: var(--backdrop);
  }
  .spread {
    position: absolute; left: 61px; top: 187px;
    width: 1063px; height: 529px;
    display: flex;
    border: 1px solid var(--edge);
    background: var(--paper);
  }
  .page {
    position: relative; width: 50%; height: 100%;
    color: var(--ink);
  }
  .page--left { border-right: 1px solid var(--edge); }
  .page-marker {
    position: absolute; top: 28px; width: 46px; height: 86px;
  }
  .page--left .page-marker { left: 18px; }
  .page--right .page-marker { right: 14px; }
  .page-number {
    font-family: "Questrial", sans-serif; font-size: 11px; font-weight: 700;
    fill: var(--ink);
  }
  .quote {
    position: absolute; left: 0; right: 0; top: 104px;
    text-align: center;
    font-family: "Cormorant Infant", serif; font-style: italic; font-weight: 500;
    font-size: 35px; line-height: 43.5px;
  }
  .author-note {
    position: absolute; left: 0; right: 0; bottom: 44px;
    text-align: center;
    font-family: "Questrial", sans-serif; font-size: 13.5px; line-height: 18px;
  }
  .author-note strong { font-weight: 700; }
</style>
</head>
<body>
  <main class="spread">
    <section class="page page--left">
      <svg class="page-marker" viewBox="0 0 46 86" aria-hidden="true">
        <path d="M16 2 h20 l1 18 q0 12 -11 12 q-11 0 -11 -12 z" fill="var(--glass-light)"/>
        <path d="M2 14 h22 l1 19 q0 13 -12 13 q-12 0 -12 -13 z" fill="var(--glass-dark)"/>
        <rect x="12" y="46" width="2" height="36" fill="var(--stem)"/>
        <rect x="3" y="81" width="20" height="2" fill="var(--stem)"/>
        <text class="page-number" x="13" y="31" text-anchor="middle">1</text>
      </svg>
      <blockquote class="quote">
        The discovery of a good wine is<br>
        increasingly better for mankind<br>
        than the discovery of a new star.<br>
        – Lorenzo Valcieri
      </blockquote>
      <p class="author-note">
        <strong>Lorenzo di Matteo Valcieri</strong> (1487 –1553)<br>
        Tuscan Vintner, Cellar Master, Poet, Lutenist, Botanist,<br>
        Traveller, Merchant, Diarist, Engraver, Glassmaker,<br>
        Gardener, Bookbinder and Writer.
      </p>
    </section>
    <section class="page page--right">
      <svg class="page-marker" viewBox="0 0 46 86" aria-hidden="true">
        <path d="M22 2 h20 l1 18 q0 12 -11 12 q-11 0 -11 -12 z" fill="var(--glass-light)"/>
        <path d="M8 14 h22 l1 19 q0 13 -12 13 q-12 0 -12 -13 z" fill="var(--glass-dark)"/>
        <rect x="18" y="46" width="2" height="36" fill="var(--stem)"/>
        <rect x="9" y="81" width="20" height="2" fill="var(--stem)"/>
        <text class="page-number" x="19" y="31" text-anchor="middle">2</text>
      </svg>
      <blockquote class="quote">
        Be careful to trust a person<br>
        who does not like wine.<br>
        – Konrad Halbach
      </blockquote>
      <p class="author-note">
        <strong>Konrad Emil Halbach</strong> (1824 –1891)<br>
        Bavarian Innkeeper, Brewer, Essayist, Almanac Maker, Printer,<br>
        and Wandering Storyteller.
      </p>
    </section>
  </main>
</body>
</html>
```